Performance Coaching business needs brochure design

I need a brochure designed that will be given to attendants at an IT / Accountancy conference.
Aim: The brochure is to encourage people to take up the offer that will be on there.
My business: Velmora Vitality Coaching. I coach people in corporate jobs how to improve performance through keeping fitn and healthy.
The brochure: I will post a list of notes (2 pages) I have and the winning designer is to use these notes to take out the most important points and create a powerful, enticing brochure that meets the following guidlines:
Why staff health is important to business? You will quote stats and reasons why it is important.
What staff want from their employer?
What I do?
Case study
Enticing Offer
The winning design will use powerful images, and will be light on words. The words used will answer the above points (these points dont't necessarily need to be on the brochure in the wording I have used here).
You can use my website www.velmoravitalitycoaching.example for ideas.
Updates
Apologies but I have been advised of a slight change. I now require A4 size design. It needs to go into a folder with a lot of other information. My new requirements are:
a) 2-3 pages max. either 1 front and back and an offer page, or 2 -3 single sided pages. whatever looks best
b) page or section 1 must be about why personal health/wellbeing is important to business. Include stats from my handouts as well as reasons why
c) section 2 is about what benefit health is to staff (eg....they get more from their company, they are better at their job, their performance is enhanced etc
d) page or section 3 must include about me (from my website www.velmoravitalitycoaching.example) and results from KWT
d) section 4 is the offer to KWT delegates.
FYI KWT (company holding the conference) website is www.kwt-onward.example use it for their logo if you need
This format has been confirmed and aplogies for the change
Target Market(s)
Accountancy firms.
Industry/Entity Type
Health
Requirements
Must have
- Can be either a fold up style brochure or a flyer with front & back. Must be easy to print as I will need to print it as soon as possible.
The images supplied are just a guide...use if you like
Nice to have
- I'd like to see a design the portrays success, change, health, simplicity, clarity.

```html
<!DOCTYPE html>
<html lang="en">
<head>
<meta charset="utf-8">
<title>A Healthy Bottom Line – Velmora Vitality Coaching</title>
<link rel="stylesheet" href="https://fonts.googleapis.com/css2?family=Source+Sans+3:wght@400;600;700;800;900&family=Dancing+Script:wght@600&display=swap">
<style>
  :root {
    --ink: #1a1a1a;
    --charcoal: #4a4a4a;
    --band: #525252;
    --yellow: #f7ec2a;
    --yellow-title: #ffe81a;
    --red: #d7191f;
    --navy: #243f9c;
    --white: #ffffff;
    --muted: #3a3a3a;
    --canvas: #ffffff;
  }
  * { box-sizing: border-box; margin: 0; padding: 0; }
  html, body { width: 1200px; height: 900px; overflow: hidden; background: var(--canvas); }
  body { position: relative; font-family: "Source Sans 3", Arial, sans-serif; color: var(--ink); }

  .page { position: absolute; background: var(--white); box-shadow: 0 3px 10px rgba(0,0,0,.35); overflow: hidden; }

  /* Page 1 */
  .page--intro { left: 12px; top: 10px; width: 410px; height: 580px; }
  .page-title { height: 66px; background: var(--band); color: var(--yellow-title); font-weight: 800; font-size: 34px; line-height: 66px; padding-left: 22px; }
  .hero-photo { height: 246px; background: linear-gradient(135deg, #dfe6ee 0%, #b9c6d3 45%, #5b6b80 70%, #2a3346 100%); }
  .intro-heading { color: var(--navy); font-weight: 800; font-size: 26px; line-height: 32px; padding: 6px 0 0 44px; }
  .intro-body { display: flex; gap: 8px; padding: 4px 12px 0 18px; }
  .benefit-list { list-style: none; width: 196px; flex: none; }
  .benefit-list li, .stat-list li { color: var(--red); font-weight: 700; position: relative; }
  .benefit-list li { font-size: 16px; line-height: 19px; padding-left: 16px; }
  .benefit-list li::before, .stat-list li::before { content: "•"; position: absolute; left: 0; }
  .intro-aside { font-size: 9.5px; line-height: 11.5px; color: var(--muted); padding-top: 10px; flex: 1; }
  .intro-foot { display: flex; align-items: center; padding: 6px 14px 0 18px; gap: 10px; }
  .intro-foot p { width: 186px; flex: none; font-size: 9px; line-height: 11px; color: var(--muted); text-align: justify; }
  .brand { display: flex; align-items: center; gap: 6px; font-weight: 700; color: var(--charcoal); }
  .brand-mark { width: 12px; height: 12px; background: var(--yellow); flex: none; }
  .brand--panel { width: 180px; height: 64px; border: 1px solid #ddd; padding: 6px 8px; font-size: 19px; line-height: 21px; }
  .site-band { position: absolute; left: 0; right: 0; bottom: 0; height: 62px; background: var(--band); color: var(--white); font-weight: 700; font-size: 19px; line-height: 62px; text-align: center; }

  /* Page 2 */
  .page--stats { left: 432px; top: 68px; width: 360px; height: 580px; }
  .stat-bar { background: var(--yellow); color: #2b2b2b; font-weight: 700; margin-top: 14px; padding: 5px 10px; font-size: 14px; line-height: 17px; }
  .stat-bar:first-child { margin-top: 0; }
  .stat-bar--centered { text-align: center; }
  .stat-bar--small { font-size: 11px; padding: 5px 10px; white-space: nowrap; }
  .stat-list { list-style: none; padding: 8px 0 0 28px; }
  .stat-list li { font-size: 14.5px; line-height: 19px; padding-left: 14px; }
  .stats-inner { padding-top: 4px; }
  .cta-line { text-align: center; font-weight: 900; font-size: 32px; margin-top: 12px; letter-spacing: .5px; }
  .call-band { position: absolute; left: 0; right: 0; bottom: 0; height: 92px; background: #000; color: var(--white); display: flex; align-items: center; padding: 0 12px 0 22px; gap: 16px; }
  .call-text { flex: none; white-space: nowrap; }
  .call-text strong { display: block; font-weight: 800; font-size: 34px; line-height: 38px; }
  .call-text span { display: block; font-weight: 600; font-size: 21px; line-height: 26px; letter-spacing: 1px; }
  .brand--dark { color: var(--white); font-size: 17px; line-height: 19px; flex: 1; }

  /* Page 3 */
  .page--offer { left: 795px; top: 300px; width: 390px; height: 580px; }
  .about { background: #000; color: var(--white); height: 178px; display: flex; padding: 8px; gap: 10px; }
  .portrait { width: 176px; height: 160px; flex: none; background: linear-gradient(180deg, #9fc4e6 0%, #c9dced 45%, #6f7e66 75%, #2c2a28 100%); }
  .about-text { padding-top: 6px; }
  .coach-name { font-family: "Dancing Script", cursive; color: var(--yellow); font-size: 14px; }
  .about-text p { font-size: 9.5px; line-height: 11.5px; margin-top: 3px; }
  .about-text .tagline { font-style: italic; font-size: 14px; line-height: 17px; margin-top: 12px; }
  .result { font-size: 9.5px; line-height: 11px; color: var(--muted); padding: 4px 10px 0 20px; }
  .offer-badge { position: absolute; left: 115px; top: 222px; width: 118px; height: 118px; }
  .offer-box { position: absolute; left: 0; right: 0; top: 315px; height: 205px; background: var(--yellow); padding: 22px 16px 0 22px; font-weight: 800; font-size: 19px; line-height: 23px; color: #111; text-align: justify; }
  .offer-box em { font-style: normal; color: var(--red); }
  .offer-box .offer-close { display: block; text-align: center; font-size: 20px; margin-top: 10px; }
  .site-band--offer { height: 60px; line-height: 60px; font-size: 18px; }
</style>
</head>
<body>

<section class="page page--intro">
  <h1 class="page-title">A Healthy Bottom Line</h1>
  <div class="hero-photo" role="img" aria-label="Photo of a businessman in a suit working out on a gym machine"></div>
  <h2 class="intro-heading">Healthy and Fit Employees:</h2>
  <div class="intro-body">
    <ul class="benefit-list">
      <li>Work more efficiently</li>
      <li>Work better with others</li>
      <li>Call in sick less often</li>
      <li>Are generally happier</li>
    </ul>
    <p class="intro-aside">Business coaching and more recently EQ (emotional) coaching have become accepted employee resources so why not health coaching? Are you achieving this compared to your competitors?</p>
  </div>
  <div class="intro-foot">
    <p>For staff to function at their optimum, they must be healthy and have reasonable energy. Health coaching can provide the missing link to your staffs performance.</p>
    <div class="brand brand--panel"><span class="brand-mark"></span><span>Velmora Vitality Coaching</span></div>
  </div>
  <div class="site-band">www.velmoravitalitycoaching.example</div>
</section>

<section class="page page--stats">
  <div class="stats-inner">
    <div class="stat-bar">Studies over a 12 year period, show that companies with high-performance cultures outperformed others by:</div>
    <ul class="stat-list">
      <li>4x revenue growth</li>
      <li>8x employment growth</li>
    </ul>
    <div class="stat-bar stat-bar--centered">If your staff are fit &amp; healthy you can expect:</div>
    <ul class="stat-list">
      <li>Greater value to the business and it’s people</li>
      <li>Increased profits and ROI</li>
      <li>Increased brand recognition</li>
      <li>Workplace of choice</li>
    </ul>
    <div class="stat-bar stat-bar--small">1 in 6 employees are overworked and don’t use their vacation time</div>
    <ul class="stat-list">
      <li>62% suffer neck or back pain</li>
      <li>34% have sleep problems</li>
    </ul>
    <div class="stat-bar stat-bar--centered">Successful corporate health programs can create:</div>
    <ul class="stat-list">
      <li>26.8% reduction in absenteeism</li>
      <li>$5.81 savings on every dollar invested</li>
    </ul>
    <p class="cta-line">WE CAN HELP</p>
  </div>
  <div class="call-band">
    <div class="call-text"><strong>Call Now</strong><span>01632 960 418</span></div>
    <div class="brand brand--dark"><span class="brand-mark"></span><span>Velmora Vitality Coaching</span></div>
  </div>
</section>

<section class="page page--offer">
  <div class="about">
    <div class="portrait" role="img" aria-label="Portrait photo of the coach outdoors with a harbour behind"></div>
    <div class="about-text">
      <div class="coach-name">Dana Keller</div>
      <p>I provide companies with an opportunity to reduce the high cost of absenteeism and presenteeism. In short I help, you position your business so that it attracts and retains the highest quality staff, while increasing revenue.</p>
      <p class="tagline">...You become more, when your staff become more.</p>
    </div>
  </div>
  <p class="result">65% of people in KWT are now doing more exercise than they were 12 months ago.<br>“The energy post a lunch time work is enormous”</p>
  <div class="offer-box">
    The first 15 companies to contact Velmora Coaching will receive a <em>free assessment and post-assessment conference</em> at your office so you can see exactly how Velmora Vitality Coaching can help you...
    <span class="offer-close">Build a Healthy Bottom Line!</span>
  </div>
  <svg class="offer-badge" viewBox="0 0 120 120" aria-label="A Special Offer to KWT Delegates">
    <polygon fill="#d7191f" points="60,2 67,12 79,5 82,17 95,15 94,28 107,31 101,43 112,51 102,60 112,69 101,77 107,89 94,92 95,105 82,103 79,115 67,108 60,118 53,108 41,115 38,103 25,105 26,92 13,89 19,77 8,69 18,60 8,51 19,43 13,31 26,28 25,15 38,17 41,5 53,12"/>
    <g fill="#fff" font-family="Source Sans 3, Arial, sans-serif" font-weight="700" text-anchor="middle" transform="rotate(-18 60 60)">
      <text x="60" y="38" font-size="14">A</text>
      <text x="60" y="55" font-size="15">Special</text>
      <text x="60" y="72" font-size="15">Offer to KWT</text>
      <text x="60" y="89" font-size="15">Delegates</text>
    </g>
  </svg>
  <div class="site-band site-band--offer">www.velmoravitalitycoaching.example</div>
</section>

</body>
</html>
```